Local primary school needs a flyer design for their fundraising fete

I need a flyer design for a local primary school holding a fundraising fete. I would like to see designs that feature the school logo, school colours (red white and navy) and that reference/mention the main rides and stalls at the event. If possible I would like the sponsors (on the newsletter supplied) to be included and the photo of the school available on the website. The final design should be easy for me to print and produce myself so that can leave at local shops, cafes etc. leading up to the event.

Industry/Entity Type

School

Font styles to use
Serif

Colors
ec2027
ffffff

```html
<!DOCTYPE html>
<html lang="en">
<head>
<meta charset="utf-8">
<title>Our Great Fete – Tamsin Reach Primary School</title>
<link rel="stylesheet" href="https://fonts.googleapis.com/css2?family=Cinzel:wght@700&family=Libre+Baskerville:wght@700&family=Fredoka:wght@600&family=Oswald:wght@500;600&family=Arimo:wght@700&display=swap">
<style>
  :root {
    --yellow-light: #f1ec4a;
    --yellow-deep: #d9d626;
    --red: #d8262c;
    --red-dark: #a5161b;
    --red-shade: #6e0c10;
    --navy-blue: #2636a3;
    --ink: #1b1b1b;
    --white: #ffffff;
    --paper: #fbfbf6;
  }
  * { margin: 0; padding: 0; box-sizing: border-box; }
  html, body { width: 835px; height: 1200px; overflow: hidden; background: #eeeeee; }
  .flyer {
    position: relative;
    width: 835px;
    height: 1200px;
    overflow: hidden;
    background: radial-gradient(ellipse at 45% 30%, var(--yellow-light) 0%, var(--yellow-deep) 80%);
  }
  .lower-band {
    position: absolute; left: 0; top: 700px; width: 835px; height: 410px;
    background: linear-gradient(180deg, #e0302f 0%, var(--red) 40%, #c21e24 100%);
  }
  .web-band {
    position: absolute; left: 0; top: 1110px; width: 835px; height: 90px;
    background: var(--yellow-light);
    display: flex; align-items: center; justify-content: center;
  }
  .web-address {
    font-family: "Arimo", Arial, sans-serif;
    font-weight: 700; font-size: 42px; color: var(--ink); letter-spacing: 0.5px;
  }
  .ribbon { position: absolute; left: 95px; top: 38px; width: 645px; height: 110px; }
  .school-name {
    position: absolute; left: 140px; top: 66px; width: 555px; text-align: center;
    font-family: "Cinzel", Georgia, serif; font-weight: 700; font-size: 27px;
    color: var(--white); letter-spacing: 0.5px; white-space: nowrap;
  }
  .presents {
    position: absolute; top: 138px; width: 835px; text-align: center;
    font-family: "Libre Baskerville", Georgia, serif; font-weight: 700; font-size: 30px;
    color: var(--ink);
  }
  .title {
    position: absolute; top: 185px; width: 835px; text-align: center;
    font-family: "Fredoka", "Arial Rounded MT Bold", sans-serif; font-weight: 600;
    font-size: 74px; line-height: 1; color: var(--navy-blue); letter-spacing: 1px;
    text-shadow: 0 3px 0 rgba(0,0,0,0.15);
  }
  .time-badge {
    position: absolute; left: 55px; top: 315px; width: 190px; height: 190px;
    border-radius: 50%; background: var(--red);
    border: 7px solid var(--white); box-shadow: 0 0 0 4px var(--red), 0 6px 12px rgba(0,0,0,0.25);
    display: flex; flex-direction: column; align-items: center; justify-content: center;
    font-family: "Oswald", "Arial Narrow", sans-serif; color: var(--yellow-light);
    text-align: center; line-height: 1.1;
  }
  .time-badge .hours { font-size: 27px; font-weight: 600; }
  .time-badge .day { font-size: 34px; font-weight: 600; }
  .time-badge .date { font-size: 17px; font-weight: 500; }
  .photo {
    position: absolute; background: var(--paper); padding: 12px 12px 34px;
    box-shadow: 0 6px 14px rgba(0,0,0,0.3);
  }
  .photo .fill { width: 100%; height: 100%; }
  .photo .pin {
    position: absolute; top: -9px; left: 50%; width: 20px; height: 20px; margin-left: -10px;
    border-radius: 50%; background: var(--red); box-shadow: 0 2px 3px rgba(0,0,0,0.4);
  }
  .photo-gift { left: 470px; top: 295px; width: 290px; height: 265px; transform: rotate(6deg); }
  .photo-gift .fill { background: linear-gradient(135deg, #f4e6d8, #d95a4a 60%, #c93a36); }
  .photo-kids { left: 35px; top: 560px; width: 260px; height: 230px; transform: rotate(-3deg); }
  .photo-kids .fill { background: linear-gradient(135deg, #f3e3d2, #e66aa8 45%, #5da8d8); }
  .photo-food { left: 305px; top: 590px; width: 225px; height: 215px; transform: rotate(1deg); }
  .photo-food .fill { background: linear-gradient(135deg, #e9ddc9, #b7b07a 45%, #c84434); }
  .photo-garden { left: 545px; top: 560px; width: 260px; height: 225px; transform: rotate(4deg); }
  .photo-garden .fill { background: linear-gradient(135deg, #9cbf5a, #4f8a2e 55%, #c73a2a); }
  .happening-heading {
    position: absolute; top: 880px; width: 835px; text-align: center;
    font-family: "Oswald", "Arial Narrow", sans-serif; font-weight: 600; font-size: 48px;
    line-height: 1.1; color: var(--yellow-light); letter-spacing: 2px;
  }
  .activities {
    position: absolute; top: 960px; left: 0; width: 835px; list-style: none;
    display: flex; flex-wrap: wrap; justify-content: center; row-gap: 16px;
    padding: 0 60px;
    font-family: "Oswald", "Arial Narrow", sans-serif; font-weight: 500; font-size: 32px;
    line-height: 1.2; color: var(--yellow-light); letter-spacing: 1px;
  }
  .activities li { display: flex; align-items: center; margin: 0 16px; }
  .activities li::before {
    content: ""; width: 22px; height: 22px; border-radius: 50%;
    background: radial-gradient(circle at 35% 35%, #fff78a, #e3c514);
    margin-right: 12px;
  }
  .activities .row-break { flex-basis: 100%; height: 0; margin: 0; }
  .activities .row-break::before { display: none; }
</style>
</head>
<body>
<main class="flyer">
  <div class="lower-band"></div>

  <svg class="ribbon" viewBox="0 0 645 110" aria-hidden="true">
    <polygon points="0,28 70,28 70,98 0,98 22,63" fill="var(--red-dark)"/>
    <polygon points="645,28 575,28 575,98 645,98 623,63" fill="var(--red-dark)"/>
    <polygon points="45,88 70,98 70,88" fill="var(--red-shade)"/>
    <polygon points="600,88 575,98 575,88" fill="var(--red-shade)"/>
    <rect x="45" y="10" width="555" height="78" fill="var(--red)"/>
  </svg>
  <div class="school-name">TAMSIN REACH PRIMARY SCHOOL</div>
  <div class="presents">presents</div>
  <h1 class="title">OUR GREAT FETE</h1>

  <div class="time-badge">
    <span class="hours">11AM – 4PM</span>
    <span class="day">SUNDAY</span>
    <span class="date">21 SEPTEMBER</span>
  </div>

  <figure class="photo photo-gift"><span class="pin"></span><div class="fill" role="img" aria-label="Child holding a wrapped gift box with a red bow"></div></figure>
  <figure class="photo photo-kids"><span class="pin"></span><div class="fill" role="img" aria-label="Group of smiling school children in a row"></div></figure>
  <figure class="photo photo-food"><span class="pin"></span><div class="fill" role="img" aria-label="Plate of fresh salad and food from the stalls"></div></figure>
  <figure class="photo photo-garden"><span class="pin"></span><div class="fill" role="img" aria-label="Boy picking strawberries in a garden"></div></figure>

  <h2 class="happening-heading">WHAT'S HAPPENING</h2>
  <ul class="activities">
    <li>Meeting</li>
    <li>Raffle</li>
    <li>Cakes</li>
    <li>Hearts</li>
    <li class="row-break" aria-hidden="true"></li>
    <li>Second Hand Books</li>
    <li>Pick-A-Pot</li>
  </ul>

  <div class="web-band"><span class="web-address">www.tamsinreachps.edu.au</span></div>
</main>
</body>
</html>
```